High End, Contemporary Fitness Boutique 3 Panel Brochure

I have included the copy and images needed; I'm definitely no designer so it's laughable in its current state. What I'm in need of is for somebody to take the current idea and copy, and turn it into a polished high-end brochure to help educate clients and markets before a studio opens. So the copy is set, but placement (within each panel) and font, colors, design, etc are all up to you! I need your help! Thanks for checking out this project, I'll be guaranteeing this as soon as I get something back that I like, before we begin fine-tuning the design. Also, if there are any spelling or grammar changes you'd like to see, I'm open to that.

Target Market(s)

Upscale Coastal Women, 30-55, with desposible income

Industry/Entity Type

Boutique

Colors
fdf9cf
ffffff
cee9f5

Requirements
Must have
• the Blue Color is Pantone 630C, Grey is Panton 430C, I don't have a Pantone for the Yellow, I'm still looking for something soft, appealing, upmarket, and splashy to contrast (in limited supply) the Blue(630C)
Nice to have
• Uniform Look & Feel, page-turning design
Should not have
• goofy splashy graphics or fonts, salesey pitch pieces

```html
<!DOCTYPE html>
<html lang="en">
<head>
<meta charset="utf-8">
<title>EvenKeel Program – Inside Spread</title>
<link href="https://fonts.googleapis.com/css2?family=Days+One&family=Oswald:wght@400;500&display=swap" rel="stylesheet">
<style>
  :root {
    --teal: #33afd0;
    --teal-deep: #1d8aa6;
    --sky: #cee9f5;
    --ink: #1c1c1c;
    --paper: #ffffff;
    --backdrop: #ececec;
  }
  * { box-sizing: border-box; margin: 0; padding: 0; }
  html, body { width: 1200px; height: 900px; overflow: hidden; background: var(--backdrop); }
  .spread {
    position: absolute; left: 50px; top: 22px; width: 1100px; height: 856px;
    background: var(--paper); overflow: hidden;
    box-shadow: 0 4px 18px rgba(0,0,0,.18);
  }
  .spread-art { position: absolute; inset: 0; }
  .panel { position: absolute; top: 73px; }
  .panel--left { left: 23px; width: 322px; }
  .panel--middle { left: 388px; width: 336px; }
  .panel--right { left: 747px; width: 336px; }
  .heading {
    font-family: "Days One", sans-serif; font-variant: small-caps;
    color: var(--teal); font-size: 31px; line-height: 36px; font-weight: 400;
    letter-spacing: .5px;
  }
  .body-copy {
    font-family: "Oswald", sans-serif; font-size: 13.6px; line-height: 23px;
    color: var(--ink); text-align: justify; margin-top: 10px;
  }
  .body-copy--small { font-size: 12.4px; line-height: 20.5px; }
  .panel--left .body-copy { margin-top: 23px; }
  .section-lower { position: absolute; top: 286px; width: 100%; }
  .testimonial {
    position: absolute; top: 265px; left: 0;
    font-family: "Oswald", sans-serif; color: var(--ink); font-size: 11px;
  }
  .testimonial q { color: var(--teal); font-style: italic; font-size: 17px; quotes: "\201C" "\201D"; }
  .promise {
    position: absolute; left: 625px; top: 614px; width: 450px; height: 144px;
    background: var(--teal); border-radius: 6px; padding: 8px;
  }
  .promise-inner {
    height: 100%; border: 2px dashed rgba(255,255,255,.85); border-radius: 4px;
    display: flex; align-items: center; justify-content: flex-end; padding-right: 16px;
    font-family: "Days One", sans-serif; font-variant: small-caps;
    color: var(--paper); font-size: 30px; line-height: 38px; text-align: right;
  }
</style>
</head>
<body>
<main class="spread">
  <svg class="spread-art" viewBox="0 0 1100 856" width="1100" height="856" aria-hidden="false">
    <defs>
      <linearGradient id="fold" x1="0" x2="1">
        <stop offset="0" stop-color="#000" stop-opacity="0"/>
        <stop offset=".5" stop-color="#000" stop-opacity=".06"/>
        <stop offset="1" stop-color="#000" stop-opacity="0"/>
      </linearGradient>
      <linearGradient id="portrait" x1="0" y1="0" x2="0" y2="1">
        <stop offset="0" stop-color="#e9b9a3"/>
        <stop offset=".45" stop-color="#e0528a"/>
        <stop offset="1" stop-color="#4a4a4e"/>
      </linearGradient>
    </defs>
    <path class="top-band" d="M0 0H1080a20 20 0 0 1 20 20V46H0Z" fill="var(--teal)"/>
    <polygon class="sky-wedge" points="0,470 380,805 0,805" fill="var(--sky)"/>
    <polygon class="deep-wedge" points="17,730 371,567 596,816" fill="var(--teal-deep)"/>
    <polygon class="light-sweep" points="371,770 1100,790 1100,856 371,856" fill="#5cc0dc"/>
    <polygon class="base-band" points="0,720 596,812 1100,826 1100,856 0,856" fill="var(--teal)"/>
    <rect x="52" y="359" width="307" height="382" rx="10" fill="url(#portrait)" role="img" aria-label="Photo of a smiling woman in a pink top flexing her arm while holding out the waistband of oversized jeans"/>
    <rect class="fold" x="358" y="0" width="30" height="856" fill="url(#fold)"/>
    <rect class="fold" x="722" y="0" width="30" height="856" fill="url(#fold)"/>
  </svg>

  <section class="panel panel--left">
    <h2 class="heading">Live your life in<br>Balance!</h2>
    <p class="body-copy">Dana was able to lose over 25lbs, and just completed her first 10K race! The 4 Pillars of the EvenKeel Program proved that even though she was never active or athletic before, her Summit Line Trainers showed her the way to live the fittest and healthiest life for herself and her family!</p>
    <p class="testimonial"><q>If I could do it, so can YOU!</q> – Dana R.</p>
  </section>

  <section class="panel panel--middle">
    <h2 class="heading">Toning!</h2>
    <p class="body-copy">Working with one of our Summit Line Personal Trainers, you will perform a complete &amp; thorough functional training workout to start each session, that will strengthen your muscles and joints, elevate your poise &amp; posture, and activate all that beautiful Metabolically Active Tissue (Muscle Tone!). The advantage of your Toning Exercises is that your body requires more fuel to move that added muscle-tone! So the same tasks you perform today, will require more calories to perform tomorrow! WOW!</p>
    <div class="section-lower">
      <h2 class="heading">Cardio Intervals!</h2>
      <p class="body-copy body-copy--small">Cardio is important for so many reasons; Heart Health, Lung Health, Circulation.. But the tangible benefit is Fat Burning! We take Cardio a step further; our Summit Line Trainers work with you on Ellipticals, Treadmills and Bikes to perform specifically designed intervals of high and low cardio effort suited to your baseline! This essentially plays a trick on your body, revving your metabolism to a point where you reach that 'afterburn' (see: EPOC). This metabolic state burns the calories as if you were to continue running for an additional two hours, WOW!</p>
    </div>
  </section>

  <section class="panel panel--right">
    <h2 class="heading">Nutrition!</h2>
    <p class="body-copy body-copy--small">The most important pillar of your successful transformation is understanding nutrition's role in the program. Our Summit Line Trainers will guide you through understanding energy, and how to time the foods you love, so that they work for you, and not against you! We provide nutrition counseling, helpful meal prep tips, delicious family recipes that will become dinner table favorites, and snacks that will keep you from raiding the pantry late at night!</p>
    <div class="section-lower">
      <h2 class="heading">Consistency!</h2>
      <p class="body-copy body-copy--small">Consistency!<br>The above pillars of the EvenKeel Program are vital on their own, but the real difference comes when you string them together in a consistent schedule, week after week! Our Summit Line Trainers and Studio Consultants work with you through each of these pillars to hold you accountable to maintaining your consistency, so you see the results you are working for.</p>
    </div>
  </section>

  <aside class="promise">
    <p class="promise-inner">Our team is<br>dedicated to you,<br>and your results.</p>
  </aside>
</main>
</body>
</html>
```